BRAMBLE COFFEE Menu Re-Design (drive-thru coffee shop)

* Keep style of old menu and fonts

* Change to new layout with orange outlines around each product section. I want the orange outlines to look like the orange circle around the "tax not included" on the old menu. I've attached "NEW menu layout 1" for reference.

* Change to new layout, products, sizes, and prices. I attached "Bramble Menu NEW" for reference.

* Change background color of menu from dark blue to light/medium grey

* Change to new logo (my attachment has 3 logos. Use the top/1st logo please).

Let me know if there are any questions about anything or if you need different file types.

Thank you!

Industry/Entity Type

Coffee

Font styles to use
Other font styles liked:
• High Voltage (I've attached the font in the brief.)

Colors
F0912C
F2A743
F7CA91
FBE8D2
FDF5EE

Requirements
Must have
• Grey, Orange and White theme.
Should not have
• The color black

```html
<!DOCTYPE html>
<html lang="en">
<head>
<meta charset="utf-8">
<title>Bramble Coffee Menu</title>
<link href="https://fonts.googleapis.com/css2?family=Archivo:wght@600;700;800&display=swap" rel="stylesheet">
<style>
:root{
  --orange:#ee5326;
  --grey:#5a5a5c;
  --grey-dark:#4b4b4d;
  --line:#3f3f41;
  --white:#ffffff;
  --stage:#d9d9d9;
}
*{margin:0;padding:0;box-sizing:border-box}
html,body{width:687px;height:1200px;overflow:hidden;background:var(--stage)}
body{position:relative;font-family:"Archivo",Arial,sans-serif;color:var(--white);font-weight:700}
.menu{position:absolute;left:27px;top:0;width:633px;height:1200px;background:var(--grey);overflow:hidden}
.header{position:absolute;left:0;top:0;width:633px;height:267px;background:linear-gradient(160deg,#4a4a4c 0%,#606062 55%,#565658 100%)}
.brand-mark{position:absolute;left:150px;top:95px;width:86px;height:86px;border-radius:50%;background:var(--orange)}
.brand-name{position:absolute;left:262px;top:78px;color:var(--orange);font-weight:800;line-height:.9;text-align:center}
.brand-name .big{display:block;font-size:62px;letter-spacing:-1px}
.brand-name .small{display:block;font-size:30px;letter-spacing:6px;margin-top:8px}
.band{position:absolute;left:0;width:633px;background:var(--orange)}
.panel{position:absolute;left:0;width:633px;background:var(--grey)}
.panel.deep{background:linear-gradient(180deg,var(--grey-dark),var(--grey))}
.sizes-band{position:absolute;left:0;top:1123px;width:633px;height:77px;background:var(--orange)}
.divider{position:absolute;top:0;bottom:0;width:1px;background:var(--line)}
.t{position:absolute;white-space:nowrap;line-height:1.35}
.c{transform:translateX(-50%);text-align:center}
.r{text-align:right}
.h1{font-size:17px;font-weight:800}
.h2{font-size:11px;font-weight:800}
.h3{font-size:10px;font-weight:800}
.s{font-size:5.6px}
.xs{font-size:4.2px}
.price{font-size:5.6px;font-weight:600}
.grid{position:absolute;display:grid;font-size:5.6px;line-height:1.7;white-space:nowrap}
.grid span{text-align:center}
.list{position:absolute;font-size:5.6px;line-height:1.68;white-space:nowrap}
</style>
</head>
<body>
<div class="menu">

  <section class="header" role="img" aria-label="Dark grey header with geometric triangle and zigzag pattern">
    <div class="brand-mark"></div>
    <div class="brand-name"><span class="big">BRAMBLE</span><span class="small">COFFEE</span></div>
  </section>

  <div class="band" style="top:267px;height:39px">
    <div class="t c h3" style="left:130px;top:8px">ESPRESSO HOT | ICED</div>
    <div class="t c xs" style="left:130px;top:22px">ADD ANY FLAVORS</div>
    <div class="t c h3" style="left:438px;top:12px">FROZEN ESPRESSO</div>
  </div>
  <div class="panel" style="top:306px;height:86px">
    <div class="grid" style="left:50px;top:2px;grid-template-columns:52px 48px 48px 48px">
      <span></span><span>SMALL</span><span>MEDIUM</span><span>LARGE</span>
      <span style="text-align:right">MOCHA</span><span class="price">3,95 US$</span><span class="price">4,45 US$</span><span class="price">5,45 US$</span>
      <span style="text-align:right">LATTE</span><span class="price">3,95 US$</span><span class="price">4,45 US$</span><span class="price">5,45 US$</span>
      <span style="text-align:right">BREVE</span><span class="price">3,95 US$</span><span class="price">4,45 US$</span><span class="price">5,45 US$</span>
      <span style="text-align:right">MACCHIATO</span><span class="price">3,95 US$</span><span class="price">4,45 US$</span><span class="price">5,45 US$</span>
      <span style="text-align:right">CAPPUCINO</span><span class="price">3,70 US$</span><span class="price">4,20 US$</span><span class="price">5,20 US$</span>
      <span style="text-align:right">AMERICANO</span><span class="price">2,45 US$</span><span class="price">2,95 US$</span><span class="price">3,95 US$</span>
      <span style="text-align:right">ESPRESSO</span><span class="price">1,50 US$</span><span></span><span></span>
    </div>
    <div class="divider" style="left:253px"></div>
    <div class="list" style="left:268px;top:10px">VANILLA BEAN<br>MOCHA<br>WHITE CHOCOLATE<br>CARAMEL MELTDOWN<br>MINT CHOCOLATE CHIP<br>COOKIE CRUMBLE</div>
    <div class="list" style="left:377px;top:10px">PEANUT WAFER<br>CRUNCH STICK<br>PB CUP<br>COCO ALMOND<br>NSA VANILLA<br>BEAN<br>NSA MOCHA</div>
    <div class="grid" style="left:445px;top:22px;grid-template-columns:54px 54px 54px;line-height:1.3">
      <span>SMALL</span><span>MEDIUM</span><span>LARGE</span>
      <span class="xs">16oz</span><span class="xs">24oz</span><span class="xs">32oz</span>
      <span class="price">4,75 US$</span><span class="price">5,75 US$</span><span class="price">6,75 US$</span>
    </div>
  </div>

  <div class="band" style="top:392px;height:39px">
    <div class="t c h3" style="left:113px;top:6px">COLD BREW<br>NITRO COLD BREW</div>
    <div class="t c h3" style="left:295px;top:12px">DRIP COFFEE</div>
    <div class="t c h3" style="left:433px;top:12px">DAIRY FREE <span class="xs">+$.50</span></div>
    <div class="t c h3" style="left:524px;top:13px">ADD-ON'S</div>
  </div>
  <div class="panel" style="top:431px;height:48px">
    <div class="t c s" style="left:113px;top:5px">ADD ANY FLAVOR | ADD COLD FOAM +.50</div>
    <div class="grid" style="left:53px;top:14px;grid-template-columns:54px 56px 56px;line-height:1.5">
      <span>SMALL | <span class="xs">16oz</span></span><span>MEDIUM | <span class="xs">24oz</span></span><span>LARGE | <span class="xs">32oz</span></span>
      <span class="price">3,75 US$</span><span class="price">4,25 US$</span><span class="price">4,75 US$</span>
    </div>
    <div class="divider" style="left:212px"></div>
    <div class="grid" style="left:250px;top:9px;grid-template-columns:44px 44px 44px;line-height:1.3">
      <span>SMALL</span><span>MEDIUM</span><span>LARGE</span>
      <span class="xs">12oz</span><span class="xs">16oz</span><span class="xs">20oz</span>
      <span class="price">1,75 US$</span><span class="price">2,25 US$</span><span class="price">2,75 US$</span>
    </div>
    <div class="divider" style="left:380px"></div>
    <div class="list c" style="left:440px;top:3px">ALMOND<br>SOY<br>OAT<br>COCONUT</div>
    <div class="list" style="left:489px;top:3px">ESPRESSO SHOT | $.50<br>EXTRA FLAVOR | Free<br>WHIPPED CREAM | Free<br>SWEET CREAM COLD FOAM | $.50</div>
  </div>

  <div class="band" style="top:479px;height:39px">
    <div class="t c h1" style="left:316px;top:9px">SYRUPS &amp; SAUCES</div>
  </div>
  <div class="panel" style="top:518px;height:128px">
    <div class="t c h2" style="left:87px;top:4px">SAUCES</div>
    <div class="list c" style="left:87px;top:24px">CHOCOLATE<br>WHITE CHOCOLATE<br>CARAMEL</div>
    <div class="divider" style="left:157px"></div>
    <div class="t c h2" style="left:389px;top:4px">SYRUPS</div>
    <div class="list" style="left:182px;top:24px">ALMOND<br>ALMOND BRITTLE<br>AMARETTO<br>BROWN SUGAR<br>CINNAMON<br>BUTTER PECAN<br>BUTTER RUM<br>BUTTERSCOTCH<br>CARAMEL<br>CHEESECAKE</div>
    <div class="list" style="left:256px;top:24px">COOKIE DOUGH<br>CINNAMON<br>COCONUT<br>CUPCAKE<br>ENGLISH TOFFEE<br>HAZELNUT<br>HIBISCUS<br>IRISH CREAM<br>LAVENDER</div>
    <div class="list" style="left:333px;top:24px">MACADAMIA NUT<br>Maple<br>MAPLE<br>Peppermint<br>PEPPERMINT<br>SALTED CARAMEL<br>SHORTBREAD<br>TOASTED<br>MARSHMALLOW<br>VANILLA BEAN</div>
    <div class="list" style="left:413px;top:24px">APPLE<br>BANANA<br>BLACKBERRY<br>Blueberry<br>BLUEBERRY<br>CHERRY<br>COCONUT<br>GRAPE</div>
    <div class="list" style="left:479px;top:24px">GRAPEFRUIT<br>GREEN APPLE<br>GUAVA<br>KIWI<br>LEMON<br>LIME<br>MANGO<br>ORANGE</div>
    <div class="list" style="left:546px;top:24px">PASSION<br>FRUIT<br>PEACH<br>PINEAPPLE<br>POMEGRANATE<br>RASPBERRY<br>STRWBERRY<br>WATERMELON</div>
  </div>

  <div class="band" style="top:646px;height:39px">
    <div class="t c h3" style="left:86px;top:6px;line-height:1.25">SUGAR FREE<br>SAUCES</div>
    <div class="t c h1" style="left:316px;top:9px">SUGAR FREE SYRUPS</div>
  </div>
  <div class="panel" style="top:685px;height:54px">
    <div class="list c" style="left:87px;top:5px">CHOCOLATE<br>WHITE CHOCOLATE<br>CARAMEL</div>
    <div class="divider" style="left:157px"></div>
    <div class="list" style="left:182px;top:5px">ALMOND BRITTLE<br>CARAMEL<br>COCONUT<br>ENGLISH TOFFEE<br>HAZELNUT</div>
    <div class="list" style="left:256px;top:5px">IRISH CREAM<br>PEPPERMINT<br>SALTED CARAMEL<br>VANILLA BEAN</div>
    <div class="list" style="left:333px;top:5px">BLUE RASPBERRY<br>COCONUT<br>LEMON<br>LIME</div>
    <div class="list" style="left:413px;top:5px">MANGO<br>ORANGE<br>PEACH<br>RASPBERRY</div>
    <div class="list" style="left:479px;top:5px">STRWBERRY<br>WATERMELON</div>
  </div>

  <div class="band" style="top:739px;height:39px">
    <div class="t c h1" style="left:316px;top:9px">TEA</div>
  </div>
  <div class="panel" style="top:778px;height:67px">
    <div class="t h2" style="left:44px;top:2px">CHAI <span style="font-size:5px">HOT | ICED +$.50 | FROZEN +$1</span></div>
    <div class="list" style="left:20px;top:23px">SPICED<br>CHOCOLATE<br>RASPBERRY</div>
    <div class="list" style="left:71px;top:23px">VANILLA<br>NSA<br>VANILLA</div>
    <div class="grid" style="left:100px;top:23px;grid-template-columns:34px 34px 34px;line-height:1.5">
      <span>SMALL</span><span>MEDIUM</span><span>LARGE</span>
      <span class="price">3,75 US$</span><span class="price">4,50 US$</span><span class="price">5,50 US$</span>
    </div>
    <div class="divider" style="left:204px"></div>
    <div class="t c h2" style="left:326px;top:2px">HOT TEA</div>
    <div class="list" style="left:213px;top:17px;line-height:1.45">ENGLISH<br>BREAKFAST<br>EARL GREY<br>SWEET<br>CINNAMON</div>
    <div class="list" style="left:275px;top:26px">GREEN TEA<br>MINT<br>PEACH</div>
    <div class="grid" style="left:318px;top:26px;grid-template-columns:40px 40px 40px;line-height:1.3">
      <span>SMALL</span><span>MEDIUM</span><span>LARGE</span>
      <span class="xs">12oz</span><span class="xs">16oz</span><span class="xs">20oz</span>
      <span class="price">2,25 US$</span><span class="price">2,75 US$</span><span class="price">2,95 US$</span>
    </div>
    <div class="divider" style="left:448px"></div>
    <div class="t c h2" style="left:534px;top:2px">ICED TEA</div>
    <div class="t c" style="left:534px;top:16px;font-size:5px">ADD ANY FLAVOR</div>
    <div class="list" style="left:456px;top:30px;line-height:1.3">BLACK<br>TEA<br>GREEN<br>TEA</div>
    <div class="grid" style="left:504px;top:29px;grid-template-columns:35px 35px 35px;line-height:1.3">
      <span>SMALL</span><span>MEDIUM</span><span>LARGE</span>
      <span class="xs">16oz</span><span class="xs">24oz</span><span class="xs">32oz</span>
      <span class="price">2,95 US$</span><span class="price">3,25 US$</span><span class="price">3,50 US$</span>
    </div>
  </div>

  <div class="band" style="top:845px;height:48px">
    <div class="t c h1" style="left:316px;top:5px;font-size:15px;line-height:1.15">PUREFRUIT SMOOTHIES<br>HANDCRAFTED LEMONADE <span style="font-size:6.5px">ICED | FROZEN +$.50</span></div>
  </div>
  <div class="panel" style="top:893px;height:42px">
    <div class="list" style="left:37px;top:2px;line-height:1.45">STRAWBERRY<br>STRAWBERRY<br>BANANA<br>PEACH</div>
    <div class="list c" style="left:118px;top:2px;line-height:1.45">MANGO<br>SUPERFRUIT<br>TROPICAL</div>
    <div class="grid" style="left:160px;top:2px;grid-template-columns:41px 41px 41px;line-height:1.3">
      <span>SMALL |</span><span>MEDIUM |</span><span>LARGE |</span>
      <span class="xs">16oz</span><span class="xs">24oz</span><span class="xs">32oz</span>
      <span class="price">5,75 US$</span><span class="price">6,75 US$</span><span class="price">7,75 US$</span>
    </div>
    <div class="divider" style="left:287px"></div>
    <div class="list" style="left:303px;top:2px;line-height:1.45">ORIGINAL<br>BLUE<br>RASPBERRY<br>BLACKBERRY</div>
    <div class="list" style="left:378px;top:2px;line-height:1.45">STRAWBERRY<br>PEACH<br>CHERRY</div>
    <div class="grid" style="left:440px;top:2px;grid-template-columns:45px 45px 45px;line-height:1.3">
      <span>SMALL</span><span>MEDIUM</span><span>LARGE</span>
      <span class="xs">16oz</span><span class="xs">24oz</span><span class="xs">32oz</span>
      <span class="price">2,75 US$</span><span class="price">3,25 US$</span><span class="price">4,00 US$</span>
    </div>
  </div>

  <div class="band" style="top:935px;height:38px">
    <div class="t c h2" style="left:316px;top:12px;font-size:13px">BRAMBLE ENERGY SODAS <span style="font-size:6.5px">ICED | FROZEN</span></div>
  </div>
  <div class="panel deep" style="top:973px;height:55px">
    <div class="t c h3" style="left:84px;top:2px;line-height:1.1">VOLT RUSH</div>
    <div class="t c s" style="left:84px;top:13px">ICED | FROZEN</div>
    <div class="grid" style="left:34px;top:20px;grid-template-columns:50px 50px;line-height:1.25">
      <span>SMALL | <span class="xs">24oz</span></span><span>LARGE | <span class="xs">32oz</span></span>
      <span class="xs">1 CAN</span><span class="xs">2 CANS</span>
      <span class="price">5,95 US$</span><span class="price">7,95 US$</span>
    </div>
    <div class="divider" style="left:155px"></div>
    <div class="t c h3" style="left:216px;top:2px;line-height:1.05">PETAL<br>ENERGY</div>
    <div class="grid" style="left:166px;top:24px;grid-template-columns:50px 50px;line-height:1.45">
      <span>SMALL | <span class="xs">24oz</span></span><span>LARGE | <span class="xs">32oz</span></span>
      <span class="price">5,75 US$</span><span class="price">6,75 US$</span>
    </div>
    <div class="divider" style="left:272px"></div>
    <div class="t c s" style="left:447px;top:4px;font-size:6.5px">INFUSE WITH ANY FRUIT FLAVORS</div>
    <div class="t c s" style="left:447px;top:21px;font-size:6px;line-height:1.4">ADD TOPPER:<br>WHIPPED CREAM &nbsp;| &nbsp;CREAM &nbsp;| &nbsp;SWEET CREAM COLD FOAM &nbsp;| &nbsp;ORANGE JUICE +$.50 &nbsp;|<br>LEMONADE +$.50</div>
  </div>

  <div class="band" style="top:1028px;height:39px">
    <div class="t c h1" style="left:113px;top:4px;font-size:15px">HOT CHOCOLATE</div>
    <div class="t c" style="left:113px;top:25px;font-size:5px">TRY A "FROZEN" HOT CHOCOLATE +$.50</div>
    <div class="t c h1" style="left:315px;top:4px;font-size:15px">ITALIAN SODAS</div>
    <div class="t c" style="left:315px;top:25px;font-size:5px">INFUSE WITH ANY FLAVORS</div>
    <div class="t c h1" style="left:527px;top:4px;font-size:15px">KIDS</div>
    <div class="t c xs" style="left:527px;top:25px">ALL DRINKS COME WITH WHIP CREAM AND SPRINKLES</div>
  </div>
  <div class="panel deep" style="top:1067px;height:56px">
    <div class="t c s" style="left:113px;top:6px">ADD ANY FLAVOR</div>
    <div class="grid" style="left:35px;top:15px;grid-template-columns:55px 55px 55px;line-height:1.5">
      <span>SMALL</span><span>MEDIUM</span><span>LARGE</span>
      <span class="price">2,75 US$</span><span class="price">3,25 US$</span><span class="price">3,75 US$</span>
    </div>
    <div class="divider" style="left:198px"></div>
    <div class="t c s" style="left:315px;top:6px">WITH OR WITHOUT CREAM</div>
    <div class="grid" style="left:242px;top:15px;grid-template-columns:49px 49px 49px;line-height:1.5">
      <span>SMALL | <span class="xs">16oz</span></span><span>MEDIUM | <span class="xs">24oz</span></span><span>LARGE | <span class="xs">32oz</span></span>
      <span class="price">2,95 US$</span><span class="price">3,45 US$</span><span class="price">3,95 US$</span>
    </div>
    <div class="divider" style="left:431px"></div>
    <div class="list" style="left:447px;top:15px;line-height:1.75">PUREFRUIT SMOOTHIE | <span class="xs">ANY FLAVOR</span><br>STEAMER | <span class="xs">ANY FLAVOR + WARM STEAMED MILK</span></div>
    <div class="list price" style="left:571px;top:15px;line-height:1.75">2,95 US$<br>2,25 US$</div>
  </div>

  <div class="sizes-band">
    <div class="t c h1" style="left:316px;top:15px;font-size:14px">SIZES:</div>
    <div class="t r" style="left:200px;top:38px;width:36px;font-size:7px;line-height:1.7">HOT |<br>COLD |</div>
    <div class="grid" style="left:240px;top:40px;grid-template-columns:44px 50px 50px;line-height:1.9">
      <span>SMALL | <span class="xs">12oz</span></span><span>MEDIUM | <span class="xs">16oz</span></span><span>LARGE | <span class="xs">20oz</span></span>
      <span>SMALL | <span class="xs">16oz</span></span><span>MEDIUM | <span class="xs">24oz</span></span><span>LARGE | <span class="xs">32oz</span></span>
    </div>
  </div>

</div>
</body>
</html>
```